Brindle Offers is an online marketing platform.

A daily deals site for consumers a way to bring in new clients for clients and this is who the business cards are for. Industries - Food and Drink, Things To Do, Beauty and Spas, Staycations and Services.
Logo on one side.
Name - Owen Radley
Job Title - Sales Director
Phone Number - 07912358046
Email - owen@brindleoffers.co.uk
need same for second person
Name - Fiona Bracken
Job Title - Operations Director
Phone Number - 01632840275
Email - fiona@brindleoffers.co.uk
Bottom Right - Chatterbook Icon, Snapa Icon, Pipline Icon
Target Market(s)
Business owners of the above industries
Contact Information for Business Card
Name - Owen Radley
Name - Fiona Bracken
Look and feel

```html
<!DOCTYPE html>
<html lang="en">
<head>
<meta charset="utf-8">
<title>Brindle Offers – Business Card</title>
<link rel="stylesheet" href="https://fonts.googleapis.com/css2?family=Open+Sans:wght@400;600;700&display=swap">
<style>
  :root {
    --ink: #000000;
    --brand-blue: #0b55a8;
    --paper: #f7f7f7;
    --grey-text: #555555;
    --rule-grey: #3a3a3a;
    --white: #ffffff;
    --stage: #e4e4e4;
  }
  * { margin: 0; padding: 0; box-sizing: border-box; }
  html, body {
    width: 1200px; height: 900px; overflow: hidden;
    background: var(--stage);
    font-family: "Open Sans", Arial, sans-serif;
  }
  .canvas { position: relative; width: 1200px; height: 900px; }
  .card {
    position: absolute; left: 290px; width: 620px; height: 365px;
    overflow: hidden; box-shadow: 0 10px 28px rgba(0,0,0,.25);
  }
  .card--front { top: 50px; background: var(--paper); }
  .card--back { top: 485px; background: var(--ink); }
  .card__shapes { position: absolute; inset: 0; }

  .contact-list {
    position: absolute; right: 432px; top: 108px;
    list-style: none; text-align: right; color: var(--white);
    font-size: 13px; line-height: 40px; letter-spacing: .3px;
  }

  .person { position: absolute; right: 36px; top: 30px; text-align: right; }
  .person__name {
    font-size: 22px; color: var(--ink); letter-spacing: -.3px;
    border-bottom: 3px solid var(--brand-blue); padding: 0 4px 2px 10px;
    line-height: 1.1;
  }
  .person__name strong { font-weight: 700; }
  .person__name span { font-weight: 400; }
  .person__role { font-size: 12px; color: var(--grey-text); margin-top: 3px; letter-spacing: .3px; }

  .brand {
    position: absolute; display: flex; align-items: center;
    color: var(--brand-blue); font-weight: 700; white-space: nowrap;
  }
  .brand__dot { border-radius: 50%; border: 3px solid var(--brand-blue); flex: none; }
  .card--front .brand { left: 326px; top: 178px; font-size: 28px; gap: 10px; }
  .card--front .brand__dot { width: 26px; height: 26px; }
  .card--back .brand { left: 0; right: 0; justify-content: center; top: 110px; font-size: 46px; gap: 16px; }
  .card--back .brand__dot { width: 42px; height: 42px; }

  .social {
    position: absolute; right: 30px; bottom: 30px; display: flex; gap: 12px;
    list-style: none; font-size: 11px; font-weight: 600; color: var(--brand-blue);
  }

  .web-band {
    position: absolute; left: 0; right: 0; bottom: 0; height: 78px;
    background: var(--brand-blue); color: var(--white);
    font-size: 22px; font-weight: 600; text-align: center; padding-top: 4px;
  }
</style>
</head>
<body>
<main class="canvas">

  <section class="card card--front" aria-label="Business card front">
    <svg class="card__shapes" viewBox="0 0 620 365" width="620" height="365" aria-hidden="true">
      <rect x="0" y="0" width="10" height="365" fill="var(--brand-blue)"/>
      <polygon points="10,0 205,0 255,365 10,365" fill="var(--ink)"/>
      <line x1="214" y1="0" x2="264" y2="365" stroke="var(--brand-blue)" stroke-width="4"/>
      <line x1="300" y1="150" x2="300" y2="262" stroke="var(--rule-grey)" stroke-width="3"/>

      <g class="contact-icon contact-icon--phone" transform="translate(222 121)">
        <circle r="16" fill="var(--ink)" stroke="var(--white)" stroke-width="1.5"/>
        <rect x="-5" y="-9" width="10" height="18" rx="2" fill="none" stroke="var(--white)" stroke-width="2"/>
        <circle cx="0" cy="5.5" r="1.2" fill="var(--white)"/>
      </g>
      <g class="contact-icon contact-icon--mail" transform="translate(227 161)">
        <circle r="16" fill="var(--ink)" stroke="var(--white)" stroke-width="1.5"/>
        <rect x="-8" y="-6" width="16" height="12" fill="var(--white)"/>
        <polyline points="-8,-6 0,1 8,-6" fill="none" stroke="var(--ink)" stroke-width="1.5"/>
      </g>
      <g class="contact-icon contact-icon--web" transform="translate(233 201)">
        <circle r="16" fill="var(--ink)" stroke="var(--white)" stroke-width="1.5"/>
        <g fill="none" stroke="var(--white)" stroke-width="1.4">
          <circle r="8.5"/>
          <ellipse rx="4" ry="8.5"/>
          <line x1="-8.5" y1="0" x2="8.5" y2="0"/>
          <line x1="-7.5" y1="-4" x2="7.5" y2="-4"/>
          <line x1="-7.5" y1="4" x2="7.5" y2="4"/>
        </g>
      </g>
    </svg>

    <ul class="contact-list">
      <li class="contact-list__phone">07912358046</li>
      <li class="contact-list__email">owen@brindleoffers.co.uk</li>
      <li class="contact-list__web">www.brindleoffers.com</li>
    </ul>

    <div class="person">
      <p class="person__name"><strong>OWEN</strong> <span>RADLEY</span></p>
      <p class="person__role">SALES DIRECTOR</p>
    </div>

    <div class="brand"><span class="brand__dot"></span>Brindle Offers</div>

    <ul class="social">
      <li>Chatterbook</li>
      <li>Snapa</li>
      <li>Pipline</li>
    </ul>
  </section>

  <section class="card card--back" aria-label="Business card back">
    <div class="brand"><span class="brand__dot"></span>Brindle Offers</div>
    <p class="web-band">www.brindleoffers.com</p>
  </section>

</main>
</body>
</html>
```